House mailers

I want an informative flyer that has ou logo on the top right with our lic number photos and a description of our services. I also want the back to say tip of the moth with only two photos I will provide. clean setup noting crowded. sample flyer below.

```html
<!DOCTYPE html>
<html lang="en">
<head>
<meta charset="utf-8">
<title>House Mailer – Front and Back</title>
<link href="https://fonts.googleapis.com/css2?family=Anton&family=Montserrat:wght@300;400;600;700;800&display=swap" rel="stylesheet">
<style>
  :root{
    --blue:#1f63f0;
    --red:#d9182a;
    --ink:#111318;
    --white:#ffffff;
    --stage:#3a3a3b;
  }
  *{box-sizing:border-box;margin:0;padding:0}
  html,body{width:844px;height:1200px;overflow:hidden}
  body{background:var(--stage);position:relative;font-family:"Montserrat",sans-serif}
  .sheet{position:absolute;top:321px;width:396px;height:557px;box-shadow:0 6px 18px rgba(0,0,0,.45)}
  .sheet--front{left:16px}
  .sheet--back{left:432px}
  .flyer{position:absolute;top:0;left:0;width:660px;height:928px;background:var(--white);
         transform:scale(.6);transform-origin:0 0;overflow:hidden}
  .flyer svg.shapes{position:absolute;inset:0}
  .abs{position:absolute}

  /* brand block */
  .brand{top:30px;right:40px;text-align:right}
  .brand__row{display:flex;align-items:center;justify-content:flex-end;gap:10px}
  .brand__mark{width:40px;height:40px;background:var(--blue)}
  .brand__name{font-weight:800;font-size:27px;line-height:1;color:var(--blue);letter-spacing:.5px}
  .brand__tag{font-weight:600;font-size:22px;color:var(--red);letter-spacing:1px;margin-top:8px}
  .brand__lic{font-size:8px;font-weight:600;color:var(--ink);margin-top:2px}

  /* headline */
  .headline{top:142px;left:376px;color:var(--white);font-family:"Anton",sans-serif;line-height:1}
  .headline__big{font-size:58px;display:block;letter-spacing:.5px}
  .headline__big + .headline__big{margin-top:4px}
  .headline__sub{font-size:29px;display:block;margin-top:10px}
  .headline__company{font-size:27px;display:block;color:var(--ink);letter-spacing:24px;margin-top:6px}

  .services-title{top:352px;left:0;width:660px;height:47px;line-height:47px;text-align:center;
                  color:var(--white);font-size:29px;font-weight:300;letter-spacing:.5px}
  .services-title b{font-weight:800}

  .service{width:150px;text-align:center}
  .service__icon{display:block;margin:0 auto}
  .service__label{font-weight:600;font-size:18px;line-height:1.05;color:var(--ink);margin-top:16px}

  /* footer */
  .contact{top:822px;left:63px;height:33px;display:flex;align-items:center;color:var(--white)}
  .contact__label{font-weight:700;font-size:18px;letter-spacing:.5px;width:172px}
  .contact__phone{font-weight:700;font-size:30px;display:flex;align-items:center;gap:8px}
  .links{top:884px;left:42px;display:flex;gap:14px;color:var(--white);font-size:15px;font-weight:400}
  .links span{display:flex;align-items:center;gap:5px}
  .license{top:858px;right:40px;text-align:center;color:var(--white);line-height:1.1}
  .license__label{font-size:22px;font-weight:300}
  .license__num{font-size:22px;font-weight:800}

  .back-title{top:36px;left:0;width:660px;text-align:center;font-family:"Anton",sans-serif;
              font-size:88px;line-height:1;color:var(--blue);letter-spacing:1px}
</style>
</head>
<body>

<!-- FRONT -->
<div class="sheet sheet--front">
 <div class="flyer">
  <svg class="shapes" width="660" height="928" viewBox="0 0 660 928">
   <defs>
    <linearGradient id="houseFill" x1="0" y1="0" x2="0" y2="1">
      <stop offset="0" stop-color="#dfe6ea"/>
      <stop offset=".55" stop-color="#7f9a94"/>
      <stop offset="1" stop-color="#4f8a3a"/>
    </linearGradient>
   </defs>
   <rect x="350" y="132" width="310" height="222" fill="var(--blue)"/>
   <polygon points="0,132 178,4 352,132 352,354 0,354" fill="var(--blue)"/>
   <polygon points="8,136 178,14 344,136 344,346 8,346" fill="var(--white)"/>
   <polygon role="img" aria-label="Photo of a two-storey stucco home with a green lawn and company yard sign"
            points="12,140 178,20 340,140 340,342 12,342" fill="url(#houseFill)"/>
   <rect x="0" y="352" width="660" height="47" fill="var(--red)"/>
   <rect x="0" y="822" width="660" height="33" fill="var(--blue)"/>
   <polygon points="0,855 455,855 565,798 660,850 660,928 0,928" fill="var(--red)"/>
  </svg>

  <div class="abs brand">
   <div class="brand__row"><span class="brand__mark"></span><span class="brand__name">COASTLINE QUAKE</span></div>
   <div class="brand__tag">HOUSE BOLTING</div>
   <div class="brand__lic">#2087315</div>
  </div>

  <h1 class="abs headline">
   <span class="headline__big">RESIDENTIAL</span>
   <span class="headline__big">FOUNDATION</span>
   <span class="headline__sub">INSPECTION AND REPAIR</span>
   <span class="headline__company">COMPANY</span>
  </h1>

  <h2 class="abs services-title">OUR <b>SERVICE</b></h2>

  <!-- row 1 -->
  <div class="abs service" style="left:34px;top:426px">
   <svg class="service__icon" width="96" height="96" viewBox="0 0 96 96"><circle cx="48" cy="48" r="45" fill="var(--blue)" stroke="var(--ink)" stroke-width="5"/><g fill="none" stroke="#fff" stroke-width="3"><path d="M28 54l20 10 20-10-20-10z"/><path d="M28 54v6l20 10 20-10v-6"/><path d="M40 26v26M48 26v30M56 26v26"/></g></svg>
   <p class="service__label">Foundation inspections</p>
  </div>
  <div class="abs service" style="left:183px;top:426px">
   <svg class="service__icon" width="96" height="96" viewBox="0 0 96 96"><circle cx="48" cy="48" r="45" fill="var(--blue)" stroke="var(--ink)" stroke-width="5"/><g fill="none" stroke="#fff" stroke-width="3"><path d="M24 46l24-20 24 20"/><path d="M30 42v24h36V42"/><rect x="42" y="50" width="12" height="16"/></g></svg>
   <p class="service__label">House Bolting</p>
  </div>
  <div class="abs service" style="left:332px;top:426px">
   <svg class="service__icon" width="96" height="96" viewBox="0 0 96 96"><circle cx="48" cy="48" r="45" fill="var(--blue)" stroke="var(--ink)" stroke-width="5"/><g fill="none" stroke="#fff" stroke-width="3"><path d="M30 70V40l18-14 18 14v30"/><path d="M44 34l6 10-6 8 6 10-4 8"/></g></svg>
   <p class="service__label">Crack Repair</p>
  </div>
  <div class="abs service" style="left:478px;top:426px">
   <svg class="service__icon" width="96" height="96" viewBox="0 0 96 96"><circle cx="48" cy="48" r="45" fill="var(--blue)" stroke="var(--ink)" stroke-width="5"/><g fill="none" stroke="#fff" stroke-width="3"><path d="M26 56l30-20 14 6-30 20z"/><path d="M26 56v6l14 6 30-20v-6"/></g></svg>
   <p class="service__label">Beam Reinforcment</p>
  </div>

  <!-- row 2 -->
  <div class="abs service" style="left:34px;top:604px">
   <svg class="service__icon" width="96" height="96" viewBox="0 0 96 96"><circle cx="48" cy="48" r="45" fill="var(--blue)" stroke="var(--ink)" stroke-width="5"/><g fill="none" stroke="#fff" stroke-width="3"><path d="M24 44l24-18 24 18"/><path d="M30 40v30h36V40"/><path d="M40 70V46M56 70V46M30 52h36"/></g></svg>
   <p class="service__label">Structural Defects</p>
  </div>
  <div class="abs service" style="left:183px;top:604px">
   <svg class="service__icon" width="96" height="96" viewBox="0 0 96 96"><circle cx="48" cy="48" r="45" fill="var(--blue)" stroke="var(--ink)" stroke-width="5"/><g fill="none" stroke="#fff" stroke-width="3"><rect x="28" y="28" width="40" height="40"/><path d="M28 38h40M28 48h40M28 58h40M40 28v10M56 28v10M48 38v10M36 48v10M60 48v10M44 58v10"/></g></svg>
   <p class="service__label">Cripple Wall Bracing</p>
  </div>
  <div class="abs service" style="left:332px;top:604px">
   <svg class="service__icon" width="96" height="96" viewBox="0 0 96 96"><circle cx="48" cy="48" r="45" fill="var(--blue)" stroke="var(--ink)" stroke-width="5"/><g fill="none" stroke="#fff" stroke-width="3"><path d="M24 52h44M24 62h44M24 70h44M36 52v10M52 52v10M44 62v8M60 62v8"/><path d="M50 48l16-16M62 28l6 6"/></g></svg>
   <p class="service__label">Foundation Crack Stitching</p>
  </div>
  <div class="abs service" style="left:478px;top:604px">
   <svg class="service__icon" width="96" height="96" viewBox="0 0 96 96"><circle cx="48" cy="48" r="45" fill="var(--blue)" stroke="var(--ink)" stroke-width="5"/><g fill="none" stroke="#fff" stroke-width="3"><path d="M24 34h48M24 66h48"/><path d="M32 60l10-10h14l8 10"/><circle cx="60" cy="44" r="4"/></g></svg>
   <p class="service__label">Crawl Space Encapsulation</p>
  </div>

  <div class="abs contact">
   <span class="contact__label">CONTACT US</span>
   <span class="contact__phone"><svg width="22" height="22" viewBox="0 0 22 22"><circle cx="11" cy="11" r="11" fill="var(--ink)"/><path d="M7 6c-1 2 1 6 3 8s6 4 8 3l-1-3-3 1-3-3 1-3z" fill="#fff"/></svg>555-014-2368</span>
  </div>
  <div class="abs links">
   <span><svg width="16" height="16" viewBox="0 0 16 16"><circle cx="8" cy="8" r="8" fill="var(--ink)"/><rect x="4" y="5" width="8" height="6" fill="#fff"/></svg>hello@coastlinequake.com</span>
   <span><svg width="16" height="16" viewBox="0 0 16 16"><circle cx="8" cy="8" r="7" fill="none" stroke="var(--ink)" stroke-width="1.5"/><path d="M1 8h14M8 1c-3 4-3 10 0 14M8 1c3 4 3 10 0 14" fill="none" stroke="var(--ink)" stroke-width="1"/></svg>www.coastlinequake.com</span>
  </div>
  <div class="abs license"><div class="license__label">license No.</div><div class="license__num">#2087315</div></div>
 </div>
</div>

<!-- BACK -->
<div class="sheet sheet--back">
 <div class="flyer">
  <svg class="shapes" width="660" height="928" viewBox="0 0 660 928">
   <defs>
    <linearGradient id="crawlFill" x1="0" y1="0" x2="1" y2="1">
      <stop offset="0" stop-color="#a58a6a"/>
      <stop offset=".5" stop-color="#3a3128"/>
      <stop offset="1" stop-color="#1e1b18"/>
    </linearGradient>
    <linearGradient id="ventFill" x1="0" y1="0" x2="1" y2="1">
      <stop offset="0" stop-color="#b9b3aa"/>
      <stop offset=".6" stop-color="#8e8a85"/>
      <stop offset="1" stop-color="#a97c66"/>
    </linearGradient>
   </defs>
   <rect role="img" aria-label="Photo of a gloved hand holding a moisture meter against a wooden post in a crawl space"
         x="0" y="150" width="660" height="360" fill="url(#crawlFill)"/>
   <rect x="0" y="510" width="660" height="10" fill="var(--blue)"/>
   <rect role="img" aria-label="Photo of an inspector entering a crawl space vent beside a house wall"
         x="0" y="520" width="660" height="302" fill="url(#ventFill)"/>
   <rect x="0" y="822" width="660" height="33" fill="var(--blue)"/>
   <polygon points="0,855 455,855 565,798 660,850 660,928 0,928" fill="var(--red)"/>
  </svg>

  <h1 class="abs back-title">TIP OF THE MOTH</h1>

  <div class="abs contact">
   <span class="contact__label">CONTACT US</span>
   <span class="contact__phone"><svg width="22" height="22" viewBox="0 0 22 22"><circle cx="11" cy="11" r="11" fill="var(--ink)"/><path d="M7 6c-1 2 1 6 3 8s6 4 8 3l-1-3-3 1-3-3 1-3z" fill="#fff"/></svg>555-014-2368</span>
  </div>
  <div class="abs links">
   <span><svg width="16" height="16" viewBox="0 0 16 16"><circle cx="8" cy="8" r="8" fill="var(--ink)"/><rect x="4" y="5" width="8" height="6" fill="#fff"/></svg>hello@coastlinequake.com</span>
   <span><svg width="16" height="16" viewBox="0 0 16 16"><circle cx="8" cy="8" r="7" fill="none" stroke="var(--ink)" stroke-width="1.5"/><path d="M1 8h14M8 1c-3 4-3 10 0 14M8 1c3 4 3 10 0 14" fill="none" stroke="var(--ink)" stroke-width="1"/></svg>www.coastlinequake.com</span>
  </div>
  <div class="abs license"><div class="license__label">license No.</div><div class="license__num">#2087315</div></div>
 </div>
</div>

</body>
</html>
```